Brom-leigh Sky Harbour Custom Brokers Limited

Shop online from the USA and Ship to Jamaica
Customs Brokerage, Import Export and logistic Services
Address:- 238-240 Halden Brook Road Kingston Jamaica
Email: info@bromleighskyharbour,com
Web: www.bromleighskyharbour.com
Telephone: (876) 555-0148, (876) 555-0193
flyer should be quarter page must print information on back and front

```html
<!DOCTYPE html>
<html lang="en">
<head>
<meta charset="utf-8">
<title>Brom-leigh Sky Harbour – Business Cards</title>
<link href="https://fonts.googleapis.com/css2?family=Montserrat:wght@400;500;600;700&display=swap" rel="stylesheet">
<style>
  :root {
    --navy: #15294f;
    --gold: #e9a820;
    --band: #5b5b5b;
    --muted: #b3b3b3;
    --ink: #555;
    --paper: #ffffff;
    --backdrop: #e4e4e4;
  }
  * { box-sizing: border-box; margin: 0; padding: 0; }
  html, body { width: 1200px; height: 836px; overflow: hidden; }
  body {
    background: var(--backdrop);
    font-family: 'Montserrat', sans-serif;
    display: flex;
    align-items: center;
    justify-content: center;
    gap: 40px;
  }
  .card {
    position: relative;
    width: 540px;
    height: 309px;
    background: var(--paper);
    box-shadow: 0 2px 8px rgba(0,0,0,0.18);
    overflow: hidden;
  }
  /* brand lockup */
  .brand {
    position: absolute;
    display: flex;
    align-items: center;
    gap: 12px;
  }
  .brand-dot {
    width: 44px; height: 44px;
    border-radius: 50%;
    background: var(--navy);
    flex: none;
  }
  .brand-name {
    color: var(--navy);
    font-weight: 700;
    font-size: 19px;
    line-height: 1.2;
    text-transform: uppercase;
    letter-spacing: 0.5px;
  }
  /* front */
  .card-front .brand { left: 50%; top: 88px; transform: translateX(-50%); }
  .front-band {
    position: absolute;
    left: 0; right: 0; top: 196px;
    height: 40px;
    background: var(--band);
    display: flex;
    align-items: center;
    justify-content: space-between;
    padding: 0 24px;
    color: #fff;
  }
  .front-band .slogan { font-size: 17px; font-weight: 500; }
  .front-band svg { width: 20px; height: 20px; fill: none; stroke: #fff; stroke-width: 1.6; }
  .front-services {
    position: absolute;
    left: 0; right: 0; top: 244px;
    text-align: center;
    font-size: 11.5px;
    color: var(--muted);
    letter-spacing: 0.3px;
  }
  /* back */
  .card-back .brand { left: 50%; top: 42px; transform: translateX(-50%); }
  .back-info {
    position: absolute;
    top: 140px; left: 40px; right: 30px;
    display: flex;
    align-items: center;
  }
  .back-slogan {
    width: 150px;
    text-align: right;
    font-size: 12px;
    font-weight: 600;
    color: var(--ink);
    line-height: 1.45;
    padding-right: 16px;
    border-right: 1px solid #cfcfcf;
  }
  .contact-list { list-style: none; padding-left: 16px; }
  .contact-list li {
    display: flex; align-items: center; gap: 9px;
    font-size: 12.5px; color: var(--ink);
    line-height: 1.9;
  }
  .contact-list svg { width: 13px; height: 13px; fill: var(--ink); flex: none; }
  .back-footer-strip {
    position: absolute; left: 0; right: 0; bottom: 0;
    height: 12px; background: var(--gold);
  }
  .back-address {
    position: absolute;
    left: 48px; right: 48px; bottom: 0;
    height: 46px;
    background: var(--navy);
    border-radius: 28px 28px 0 0;
    display: flex; align-items: center; justify-content: center;
    color: #fff; font-size: 14px; font-weight: 600;
    letter-spacing: 0.3px;
  }
</style>
</head>
<body>

  <section class="card card-front">
    <div class="brand">
      <span class="brand-dot"></span>
      <span class="brand-name">Brom-leigh Sky Harbour<br>Custom Brokers Ltd.</span>
    </div>
    <div class="front-band">
      <svg viewBox="0 0 20 20" aria-hidden="true"><rect x="4" y="4" width="12" height="9" rx="1"/><path d="M2 15h16"/></svg>
      <span class="slogan">Shop online from the USA and Ship to Jamaica</span>
      <svg viewBox="0 0 20 20" aria-hidden="true" style="fill:#fff;stroke:none"><rect x="1" y="5" width="11" height="8"/><path d="M12 8h4l3 3v2h-7z"/><circle cx="5" cy="15" r="2"/><circle cx="15" cy="15" r="2"/></svg>
    </div>
    <p class="front-services">Customs Brokerage, Import Export and Logistic Services</p>
  </section>

  <section class="card card-back">
    <div class="brand">
      <span class="brand-dot"></span>
      <span class="brand-name">Brom-leigh Sky Harbour<br>Custom Brokers Ltd.</span>
    </div>
    <div class="back-info">
      <p class="back-slogan">Shop online<br>from the USA and<br>Ship to Jamaica</p>
      <ul class="contact-list">
        <li><svg viewBox="0 0 16 16" aria-hidden="true"><path d="M3 1h3l1.5 4-2 1.5a9 9 0 0 0 4 4L11 8.5l4 1.5v3a2 2 0 0 1-2 2A12 12 0 0 1 1 3a2 2 0 0 1 2-2z"/></svg>(876) 555-0148, (876) 555-0193</li>
        <li><svg viewBox="0 0 16 16" aria-hidden="true"><path d="M1 3h14v10H1z M1 3l7 6 7-6" fill="none" stroke="#555" stroke-width="1.6"/></svg>info@bromleighskyharbour,com</li>
        <li><svg viewBox="0 0 16 16" aria-hidden="true"><circle cx="8" cy="8" r="7"/></svg>www.bromleighskyharbour.com</li>
      </ul>
    </div>
    <div class="back-footer-strip"></div>
    <div class="back-address">238-240 Halden Brook Road Kingston Jamaica</div>
  </section>

</body>
</html>
```